Flyer-Design für Prozessfinanzierungsfirma
Zielgruppe
Wir sind eine Prozessfinanzierungsfirma. im Versicherungsbereich die größte Österreichs mit mehr als 50.000 Klienten und unser neues Projekt ist die Prozessfinanzierung von Patienten die durch einen Kunstfehler (Fehler von Ärzten) auf Schadenersatz klagen wollen aber nicht die Finanziellen Möglichkeiten haben.
Aufgabenstellung
Folder soll eine DIN A4 Doppelseite sein (also 4 A4 Seiten)
plus extra ein A4 Einlage Blatt Fragebogen fix vorgegebene Fragen.
#604132 Dieser Folder ist für die gleiche Firma im Bereich Versicherungen
www.heilirrtum-beispiel.at. TEXTE und DESIGN - FARBEN und INHALTE von dieser Homepage übernehmen
die Seite www.schutzbrief-muster.at ist die gleiche Prozessfinanzierungsfirma - hier gibt es bereits einen Folder. Ich lade diesen hoch...
Diese Fragen sind unbedingt 1:1 zu übernehmen für das Einlageblatt :
o Was waren meine Erkrankungen vor der Behandlung, inkl. Dauermedikation?
o Warum ging ich zum Arzt?
o Was hat mir der Arzt empfohlen?
o Wurde ich über die unterschiedlichen Behandlungsmöglichkeiten aufgeklärt?
o Was wollte ich haben?
o Was wurde gemacht?
o Was hat der Arzt aus meiner Sicht falsch gemacht?
o Was wurde als weiterer Behandlungsweg empfohlen?
o Habe ich den Arzt mit meinem Problem konfrontiert?
o Wie hat mein Arzt darauf reagiert?
o Was ist jetzt genau schlechter als vorher?
Bei dem A4 Einlageblatt sollen auf der Vorderseite und der halben Rückseite diese Fragen mit entsprechendem Platz für den Text zum ausfüllen erscheinen und die untere Hälfte der 2. Seite mit einem kurzen Slogan nochmal auf unsere Leistung aufmerksam machen - ein Feld in Kreditkartengrösse für den Empfehlungsbgeber weiss zum einkleben einer Karte freibleiben und die Firmendaten (siehe Homepage) mit Anschrift, Telefonnummer und e-mailadresse angegeben sein

```html
<!DOCTYPE html>
<html lang="de">
<head>
<meta charset="utf-8">
<title>Fragebogen – Rückseite</title>
<link href="https://fonts.googleapis.com/css2?family=Source+Sans+3:ital,wght@0,400;1,600&display=swap" rel="stylesheet">
<style>
  :root {
    --page-bg: #eceef2;
    --field-bg: #ffffff;
    --brand-red: #7b1e1e;
    --rule: #9c5a4f;
    --text: #1a1a1a;
    --light: #ffffff;
  }
  html, body { margin: 0; padding: 0; overflow: hidden; }
  body { width: 856px; height: 1200px; background: var(--page-bg); font-family: "Source Sans 3", sans-serif; }
  .sheet { position: relative; width: 856px; height: 1200px; overflow: hidden; background: var(--page-bg); }
  .question { position: absolute; left: 0; width: 856px; height: 121px; }
  .question-label { position: absolute; left: 40px; top: 28px; margin: 0; font-size: 16.5px; font-weight: 400; color: var(--text); line-height: 1; white-space: nowrap; }
  .answer-field { position: absolute; left: 72px; top: 50px; width: 732px; height: 94px; background: var(--field-bg); border-radius: 0 22px 22px 0; }
  .answer-field svg { position: absolute; left: 0; top: 0; }
  .footer-band { position: absolute; left: 0; top: 813px; width: 856px; height: 387px; background: var(--brand-red); }
  .slogan { position: absolute; left: 0; width: 856px; top: 828px; margin: 0; text-align: center; color: var(--light); font-style: italic; font-weight: 600; font-size: 31px; line-height: 44px; }
  .company-data { position: absolute; left: 53px; top: 975px; margin: 0; font-style: italic; font-weight: 600; font-size: 16px; line-height: 20.1px; color: var(--light); }
  .referral-card { position: absolute; left: 477px; top: 939px; width: 344px; height: 225px; background: var(--field-bg); border-radius: 20px; }
  .referral-label { position: absolute; left: 477px; width: 344px; top: 1041px; text-align: center; font-style: italic; font-weight: 600; font-size: 15px; line-height: 20px; color: var(--brand-red); margin: 0; }
</style>
</head>
<body>
<div class="sheet">
  <div class="question" style="top:10px">
    <p class="question-label">• Was wurde gemacht?</p>
    <div class="answer-field"><svg width="732" height="94"><g stroke="var(--rule)" stroke-width="1" stroke-dasharray="9 5"><line x1="5" y1="20" x2="726" y2="20"/><line x1="5" y1="45" x2="726" y2="45"/><line x1="5" y1="69" x2="726" y2="69"/></g></svg></div>
  </div>
  <div class="question" style="top:131px">
    <p class="question-label">• Was hat der Arzt aus meiner Sicht falsch gemacht?</p>
    <div class="answer-field"><svg width="732" height="94"><g stroke="var(--rule)" stroke-width="1" stroke-dasharray="9 5"><line x1="5" y1="20" x2="726" y2="20"/><line x1="5" y1="45" x2="726" y2="45"/><line x1="5" y1="69" x2="726" y2="69"/></g></svg></div>
  </div>
  <div class="question" style="top:251px">
    <p class="question-label">• Was wurde als weiterer Behandlungsweg empfohlen?</p>
    <div class="answer-field"><svg width="732" height="94"><g stroke="var(--rule)" stroke-width="1" stroke-dasharray="9 5"><line x1="5" y1="20" x2="726" y2="20"/><line x1="5" y1="45" x2="726" y2="45"/><line x1="5" y1="69" x2="726" y2="69"/></g></svg></div>
  </div>
  <div class="question" style="top:372px">
    <p class="question-label">• Habe ich den Arzt mit meinem Problem konfrontiert?</p>
    <div class="answer-field"><svg width="732" height="94"><g stroke="var(--rule)" stroke-width="1" stroke-dasharray="9 5"><line x1="5" y1="20" x2="726" y2="20"/><line x1="5" y1="45" x2="726" y2="45"/><line x1="5" y1="69" x2="726" y2="69"/></g></svg></div>
  </div>
  <div class="question" style="top:493px">
    <p class="question-label">• Wie hat mein Arzt darauf reagiert?</p>
    <div class="answer-field"><svg width="732" height="94"><g stroke="var(--rule)" stroke-width="1" stroke-dasharray="9 5"><line x1="5" y1="20" x2="726" y2="20"/><line x1="5" y1="45" x2="726" y2="45"/><line x1="5" y1="69" x2="726" y2="69"/></g></svg></div>
  </div>
  <div class="question" style="top:614px">
    <p class="question-label">• Was ist jetzt genau schlechter als vorher?</p>
    <div class="answer-field"><svg width="732" height="94"><g stroke="var(--rule)" stroke-width="1" stroke-dasharray="9 5"><line x1="5" y1="20" x2="726" y2="20"/><line x1="5" y1="45" x2="726" y2="45"/><line x1="5" y1="69" x2="726" y2="69"/></g></svg></div>
  </div>

  <div class="footer-band"></div>
  <h2 class="slogan">Behandlungsfehler? – Ihre Ansprüche<br>mit starker Begleitung durchsetzen!</h2>
  <p class="company-data">
    NV Rechtshilfe Finanz GmbH<br>
    FN 000000x<br>
    UID: ATU00000000<br>
    Musterplatz 12<br>
    1010 Wien<br>
    Tel: +43 (0)1/000 11 22<br>
    Fax: +43 (0)1/000 11 22-10<br>
    www.heilirrtum-beispiel.at<br>
    office@heilirrtum-beispiel.at
  </p>
  <div class="referral-card"></div>
  <p class="referral-label">empfohlen von</p>
</div>
</body>
</html>
```